Executive Business Consulting for Telco Companies and Telco Start up companies

1.) Looking for an appealing and action oriented business card design.
2.)The target companies to work with start-ups and existing companies that focus on Business to Business applications
3.) For "OKRA", a Belgium based Executive consultancy company specialised in global reach starting from the centre of Europe = Brussels.
4.) Our core competence is the Go To Market in All major global regions, incl North America, Latin America, Asia, Japan, Europe and Africa.
5.) Design should be appealing to CEO, CFO and Venture Funds signalling; Expertise, Stability, Maturity and Commitment
6.) Preferred color scheme is Blue focussed and using a modern FONT.
7.) Logo design is included (uploaded)

Target Market(s)

Telecommunication Market. Companies in a B2B business model, developping services or applications to make business run more profitable

Industry/Entity Type

Business

Contact Information for Business Card

Company Name: OKRA
Name: Joris Vandelay
Titel: Managing Director
Address: Kalkweg 58 , B-9170 Meerdonk , Belgium
Tel: + 32 471 208 364
Email: joris_vandelay@plimbox.example
LinkedIn: be.netprofilo.example/in/jorisvandelay/

Font styles to use
Serif

Colors
0455a3
3277b5

Requirements
Must have
• Second Side Text: Execute Sales Strategy and Transformation

```html
<!DOCTYPE html>
<html lang="en">
<head>
<meta charset="utf-8">
<title>OKRA – Business Card</title>
<link rel="stylesheet" href="https://fonts.googleapis.com/css2?family=Comfortaa:wght@400;700&display=swap">
<style>
  :root {
    --page-bg: #e6e6e6;
    --card-white: #f4f4f4;
    --band-grey: #7d7d7d;
    --dark-grey: #444546;
    --panel-grey: #58595a;
    --accent-blue: #3277b5;
    --brand-blue: #0455a3;
    --navy: #1c2f52;
    --text-light: #f2f2f2;
  }
  * { margin: 0; padding: 0; box-sizing: border-box; }
  html, body {
    width: 1200px; height: 1000px; overflow: hidden;
    background: var(--page-bg);
    font-family: "Comfortaa", sans-serif;
  }
  .card {
    position: absolute; left: 215px; width: 770px; height: 440px;
    background: var(--card-white);
    box-shadow: 0 6px 18px rgba(0,0,0,.18);
    overflow: hidden;
  }
  .card--front { top: 30px; }
  .card--back { top: 520px; }
  .card__art { position: absolute; inset: 0; width: 100%; height: 100%; }

  .brand { position: absolute; display: flex; align-items: center; gap: 14px; }
  .brand__dot { border-radius: 50%; background: var(--brand-blue); }
  .brand__name { font-weight: 700; color: var(--navy); letter-spacing: 2px; }

  .card--front .brand { left: 50%; top: 50%; transform: translate(-50%, -50%); }
  .card--front .brand__dot { width: 70px; height: 70px; }
  .card--front .brand__name { font-size: 86px; }

  .card--back .brand { right: 70px; top: 60px; }
  .card--back .brand__dot { width: 44px; height: 44px; }
  .card--back .brand__name { font-size: 52px; }

  .tagline {
    position: absolute; right: 72px; top: 130px; width: 200px;
    text-align: right; font-size: 13px; line-height: 19px;
    color: var(--brand-blue); font-weight: 700;
  }

  .contact { position: absolute; left: 48px; top: 108px; color: var(--text-light); }
  .contact__name { font-size: 27px; font-weight: 700; }
  .contact__title { font-size: 17px; color: var(--accent-blue); margin-top: 4px; }
  .contact__list { list-style: none; margin-top: 30px; }
  .contact__item { display: flex; align-items: center; gap: 14px; font-size: 17px; margin-bottom: 14px; }
  .contact__icon { width: 26px; height: 26px; flex: none; }
  .contact__address {
    position: absolute; left: 300px; top: 380px; font-size: 17px; color: var(--text-light);
  }
</style>
</head>
<body>

<section class="card card--front" aria-label="Card front">
  <svg class="card__art" viewBox="0 0 770 440" aria-hidden="true">
    <polygon points="560,0 680,0 770,70 770,165" fill="var(--band-grey)"/>
    <polygon points="530,0 548,0 770,178 770,186" fill="var(--accent-blue)"/>
    <polygon points="0,255 0,345 120,440 240,440" fill="var(--band-grey)"/>
    <polygon points="0,238 0,246 250,440 268,440" fill="var(--accent-blue)"/>
  </svg>
  <div class="brand">
    <span class="brand__dot"></span>
    <span class="brand__name">OKRA</span>
  </div>
</section>

<section class="card card--back" aria-label="Card back">
  <svg class="card__art" viewBox="0 0 770 440" aria-hidden="true">
    <polygon points="0,0 330,0 770,330 770,440 0,440" fill="var(--dark-grey)"/>
    <polygon points="290,0 350,0 380,38 318,38" fill="var(--accent-blue)"/>
    <rect x="0" y="95" width="400" height="85" fill="var(--panel-grey)"/>
    <rect x="270" y="360" width="500" height="60" fill="var(--panel-grey)"/>
  </svg>
  <div class="brand">
    <span class="brand__dot"></span>
    <span class="brand__name">OKRA</span>
  </div>
  <p class="tagline">Execute Sales Strategy<br>and Transformation</p>

  <div class="contact">
    <p class="contact__name">Joris Vandelay</p>
    <p class="contact__title">Managing Director</p>
    <ul class="contact__list">
      <li class="contact__item">
        <svg class="contact__icon" viewBox="0 0 26 26" aria-label="Phone">
          <circle cx="13" cy="13" r="12" fill="#f2f2f2"/>
          <path d="M9 7c1 0 1.5 2.5 1.5 3s-1 1-1 1.5 2 4 4 4 .8-1 1.5-1 3 .5 3 1.5-1.5 2-2.5 2C11 18 8 14 8 9.5 8 8 8.5 7 9 7z" fill="#444546"/>
        </svg>
        <span>+ 32 471 208 364</span>
      </li>
      <li class="contact__item">
        <svg class="contact__icon" viewBox="0 0 26 26" aria-label="Email">
          <circle cx="13" cy="13" r="12" fill="#f2f2f2"/>
          <rect x="7" y="9" width="12" height="8" fill="none" stroke="#444546" stroke-width="1.4"/>
          <path d="M7 9l6 5 6-5" fill="none" stroke="#444546" stroke-width="1.4"/>
        </svg>
        <span>joris_vandelay@plimbox.example</span>
      </li>
      <li class="contact__item">
        <svg class="contact__icon" viewBox="0 0 26 26" aria-label="Profile link">
          <circle cx="13" cy="13" r="12" fill="#f2f2f2"/>
          <g fill="none" stroke="#444546" stroke-width="1.6" stroke-linecap="round">
            <rect x="6.5" y="11" width="8" height="5" rx="2.5" transform="rotate(-45 10.5 13.5)"/>
            <rect x="11.5" y="10" width="8" height="5" rx="2.5" transform="rotate(-45 15.5 12.5)"/>
          </g>
        </svg>
        <span>be.netprofilo.example/in/jorisvandelay/</span>
      </li>
    </ul>
  </div>

  <p class="contact__address">Kalkweg 58, B-9170 Meerdonk, Belgium</p>
</section>

</body>
</html>
```